Marigold's Lantern - Foundation PPT

Design a cohesive, emotionally resonant PowerPoint template that reflects the heart of Marigold’s Lantern Pregnancy & Family Support. This template will be used across fundraising, partnership, and storytelling presentations, and must balance professionalism with warmth, compassion, and human connection.

Background
Marigold’s Lantern Pregnancy & Family Support exists to support families navigating complicated pregnancies, prolonged hospital stays, and loss. The brand is rooted in empathy, quiet strength, and the concept of a “web” of care—an interconnected support system that surrounds families during difficult moments.

The template should feel deeply personal and mission-driven, not corporate.

Design Goals
Create a visually cohesive slide system that can be reused across multiple presentation types

Capture the emotional tone of the organization:
-Warm
-Gentle
-Hopeful
-Supportive
Ensure the design is clean, minimal, and easy to use for non-designers
Maintain a balance between storytelling and credibility

Key Design Requirements
-Brand Integration: Incorporate the Marigold’s Lantern logo (provided)
Align with soft, neutral color palette (e.g., cream, sage, blush, light sky tones)
-Use elegant, readable typography

Slide Templates to Include
-Cover Slide (emotion-forward, minimal text)
-Mission / Story Slide
-Program Overview Slide
-Impact / Metrics Slide
-Partnership / Sponsor Slide
-“Web of Support” Concept Slide (visual representation of interconnected care)
-Call to Action Slide
-Optional: Quote/Testimonial Slide

Visual Style
-Soft, calming, and approachable aesthetic
-Use of whitespace to avoid clutter
-Light use of icons or illustrations (if applicable)
-Avoid overly corporate or overly busy design elements

Usability
-Fully editable in PowerPoint
-Clear text hierarchy and placeholders
-Easy for internal team to update content without design support
-Tone & Emotional Direction

This is not a clinical or corporate presentation—it should feel human, heartfelt, and intentional.

website: https://www.marigoldslanterncare.org

```html
<!DOCTYPE html>
<html lang="en">
<head>
<meta charset="utf-8">
<title>Marigold’s Lantern – Presentation Template</title>
<link href="https://fonts.googleapis.com/css2?family=Lora:wght@400;500;600&family=Nunito:wght@400;600;700;800&display=swap" rel="stylesheet">
<style>
:root{
  --canvas:#e6e6e6;
  --plum-deep:#54416b;
  --plum:#6e5785;
  --plum-mid:#8a7199;
  --lavender:#b7a1c9;
  --lavender-soft:#d9cce4;
  --blush:#d3a09d;
  --blush-soft:#ecc9c4;
  --rose-mist:#f3e5e9;
  --cream:#f7f3f1;
  --ink:#3e3346;
  --white:#ffffff;
}
*{box-sizing:border-box;margin:0;padding:0}
html,body{width:1200px;height:2647px;overflow:hidden;background:var(--canvas)}
body{position:relative;font-family:"Nunito",sans-serif;color:var(--ink)}
.slide{position:absolute;width:488px;height:275px;overflow:hidden;background:var(--cream);box-shadow:0 1px 3px rgba(0,0,0,.12)}
.slide svg.waves{position:absolute;inset:0;width:100%;height:100%}
.serif{font-family:"Lora",serif}
.slide-title{position:absolute;left:24px;top:14px;font-family:"Lora",serif;font-size:15.5px;color:var(--plum-deep);font-weight:400}
.brand{position:absolute;font-family:"Lora",serif;font-size:8px;color:var(--plum-mid);display:flex;align-items:center;gap:4px;white-space:nowrap}
.brand::before{content:"";width:9px;height:9px;border-radius:50%;border:1px solid currentColor}
.brand.light{color:#fff}
.brand.top-right{right:14px;top:14px}
.page-no{position:absolute;right:12px;bottom:6px;font-size:5px;color:var(--plum-mid)}
.flora{position:absolute;border-radius:40% 60% 50% 50%;background:radial-gradient(ellipse at center,rgba(255,255,255,.35),rgba(255,255,255,0) 70%)}
.flora.pink{background:radial-gradient(ellipse at center,rgba(211,160,157,.35),rgba(211,160,157,0) 70%)}
.hero-title{position:absolute;font-family:"Lora",serif;color:var(--blush-soft);font-size:22px;line-height:24px}
.hero-sub{position:absolute;color:#fff;font-size:11px}
.date-pill{position:absolute;background:#fff;color:var(--plum-deep);font-size:6.5px;border-radius:8px;padding:2px 8px}
.star-list{list-style:none}
.star-list li{position:relative;padding-left:13px}
.star-list li::before{content:"✱";position:absolute;left:0;top:0;color:var(--lavender);font-size:8px}
.icon-dot{border-radius:50%;display:flex;align-items:center;justify-content:center}
.icon-dot::after{content:"";width:40%;height:40%;border:1.5px solid rgba(255,255,255,.9);border-radius:30%}
.venn-label{position:absolute;width:128px;font-size:6px;line-height:7px;color:var(--plum)}
.venn-label h4{font-weight:700;font-size:9px;margin-bottom:2px}
</style>
</head>
<body>

<!-- Cover (featured) -->
<section class="slide" style="left:340px;top:68px;background:linear-gradient(180deg,#5f4a76,#7c6690)">
  <svg class="waves" viewBox="0 0 488 275" preserveAspectRatio="none">
    <defs>
      <linearGradient id="cw1" x1="0" y1="0" x2="0" y2="1"><stop offset="0" stop-color="#f6e6e3"/><stop offset="1" stop-color="#d7a3a0"/></linearGradient>
      <linearGradient id="cw2" x1="0" y1="0" x2="0" y2="1"><stop offset="0" stop-color="#e9c3bd"/><stop offset="1" stop-color="#c99491"/></linearGradient>
    </defs>
    <path d="M455 0 C400 20 420 90 380 140 C330 200 260 215 220 275 L488 275 L488 0Z" fill="url(#cw1)"/>
    <path d="M488 150 C430 170 380 220 300 240 C240 255 210 265 190 275 L488 275Z" fill="url(#cw2)" opacity=".8"/>
    <path d="M120 275 C150 250 190 250 210 275Z" fill="#8e78a2" opacity=".5"/>
  </svg>
  <div class="flora" role="img" aria-label="Line-drawn floral sprig" style="left:230px;top:130px;width:90px;height:140px"></div>
  <div class="brand light" style="left:24px;top:62px">Marigold’s Lantern</div>
  <div class="hero-title" style="left:24px;top:96px">Presentation Title<br>Goes Here</div>
  <div class="hero-sub" style="left:24px;top:152px">Sub Presentation Title Goes Here</div>
  <div class="date-pill" style="left:26px;top:182px">April, 2026</div>
</section>

<!-- Cover alternate -->
<section class="slide" style="left:78px;top:375px;background:linear-gradient(180deg,#5d4874,#715b86)">
  <svg class="waves" viewBox="0 0 488 275" preserveAspectRatio="none">
    <defs><linearGradient id="cv2" x1="0" y1="0" x2="1" y2="1"><stop offset="0" stop-color="#8a7199"/><stop offset="1" stop-color="#d6a9c0"/></linearGradient></defs>
    <path d="M420 0 C360 40 370 110 320 170 C280 220 240 240 210 275 L488 275 L488 0Z" fill="url(#cv2)" opacity=".8"/>
    <path d="M488 90 C430 140 380 210 330 275 L488 275Z" fill="#c9a1c2" opacity=".55"/>
  </svg>
  <div class="flora" role="img" aria-label="Line-drawn floral sprig" style="left:340px;top:100px;width:110px;height:170px"></div>
  <div class="brand light" style="left:24px;top:64px">Marigold’s Lantern</div>
  <div class="hero-title" style="left:24px;top:98px">Presentation Title<br>Goes Here</div>
  <div class="hero-sub" style="left:24px;top:153px">Sub Presentation Title Goes Here</div>
  <div class="date-pill" style="left:26px;top:182px">April, 2026</div>
</section>

<!-- Table of Content -->
<section class="slide" style="left:602px;top:375px;background:linear-gradient(90deg,#f5f1f3,#f6e4e8)">
  <svg class="waves" viewBox="0 0 488 275" preserveAspectRatio="none">
    <defs><linearGradient id="toc" x1="0" y1="0" x2="1" y2="0"><stop offset="0" stop-color="#c6b2d8"/><stop offset="1" stop-color="#ecdde8"/></linearGradient></defs>
    <path d="M270 0 C230 30 260 90 200 130 C130 175 90 200 70 275 L488 275 L488 0Z" fill="url(#toc)" opacity=".75"/>
    <path d="M330 0 C300 50 320 120 260 170 C220 205 200 240 190 275 L488 275 L488 0Z" fill="#f5e6eb" opacity=".8"/>
  </svg>
  <div class="flora pink" role="img" aria-label="Line-drawn floral sprig" style="left:14px;top:160px;width:60px;height:110px"></div>
  <div class="serif" style="position:absolute;left:24px;top:36px;font-size:19px;line-height:22px;color:var(--plum-deep)">Table <span style="color:var(--lavender)">✱</span><br>of Content</div>
  <div class="brand top-right">Marigold’s Lantern</div>
  <ol style="position:absolute;left:262px;top:56px;list-style:none;font-size:8px;color:var(--ink)">
    <li style="display:flex;align-items:center;gap:9px;height:36px"><span class="serif" style="width:21px;height:21px;border-radius:50%;background:var(--lavender-soft);color:var(--plum);display:flex;align-items:center;justify-content:center;font-size:11px">1</span>Lorem ipsum dolor sit amet</li>
    <li style="display:flex;align-items:center;gap:9px;height:36px"><span class="serif" style="width:21px;height:21px;border-radius:50%;background:var(--lavender-soft);color:var(--plum);display:flex;align-items:center;justify-content:center;font-size:11px">2</span>Consectetur adipiscing elit</li>
    <li style="display:flex;align-items:center;gap:9px;height:36px"><span class="serif" style="width:21px;height:21px;border-radius:50%;background:var(--lavender-soft);color:var(--plum);display:flex;align-items:center;justify-content:center;font-size:11px">3</span>Phasellus malesuada vulputate mauris</li>
    <li style="display:flex;align-items:center;gap:9px;height:36px"><span class="serif" style="width:21px;height:21px;border-radius:50%;background:var(--lavender-soft);color:var(--plum);display:flex;align-items:center;justify-content:center;font-size:11px">4</span>Vitae pretium felis vestibulum vel</li>
    <li style="display:flex;align-items:center;gap:9px;height:36px"><span class="serif" style="width:21px;height:21px;border-radius:50%;background:var(--lavender-soft);color:var(--plum);display:flex;align-items:center;justify-content:center;font-size:11px">5</span>Vestibulum non sagittis orci</li>
    <li style="display:flex;align-items:center;gap:9px;height:36px"><span class="serif" style="width:21px;height:21px;border-radius:50%;background:var(--lavender-soft);color:var(--plum);display:flex;align-items:center;justify-content:center;font-size:11px">6</span>Fusce finibus elit et felis imperdiet</li>
  </ol>
</section>

<!-- One Column -->
<section class="slide" style="left:78px;top:681px;background:#f5f3f6">
  <svg class="waves" viewBox="0 0 488 275" preserveAspectRatio="none">
    <defs><linearGradient id="oc" x1="0" y1="0" x2="0" y2="1"><stop offset="0" stop-color="#5f4a76"/><stop offset="1" stop-color="#9a7fa8"/></linearGradient></defs>
    <path d="M340 0 C320 60 400 120 340 190 C310 225 280 250 270 275 L488 275 L488 0Z" fill="url(#oc)"/>
  </svg>
  <div class="flora" role="img" aria-label="Line-drawn floral sprig" style="left:330px;top:50px;width:90px;height:170px"></div>
  <div class="slide-title">One Column Sample</div>
  <div class="brand light top-right">Marigold’s Lantern</div>
  <div style="position:absolute;left:28px;top:60px;font-weight:700;font-size:10.5px;color:var(--plum-deep)">Heading Title Here</div>
  <ul class="star-list" style="position:absolute;left:28px;top:88px;width:250px;font-size:8.5px;line-height:10px">
    <li style="margin-bottom:17px">Lorem ipsum dolor sit amet, te ullum corpora delicata duo. Rebum insolens pri eu. No alia tota modus qui.</li>
    <li style="margin-bottom:17px">Lorem ipsum dolor sit amet, te ullum corpora delicata duo. Rebum insolens pri eu. No alia tota modus qui.</li>
    <li style="margin-bottom:17px">Lorem ipsum dolor sit amet, te ullum corpora delicata duo. Rebum insolens pri eu. No alia tota modus qui.</li>
    <li>Lorem ipsum dolor sit amet, te ullum corpora delicata duo. Rebum insolens pri eu. No alia tota modus qui.</li>
  </ul>
  <div class="page-no" style="color:#fff">4</div>
</section>

<!-- Four Horizontal -->
<section class="slide" style="left:602px;top:681px;background:linear-gradient(135deg,#f5eef2,#f3e2e8)">
  <div class="slide-title">Four Horizontal Sample</div>
  <div class="brand top-right">Marigold’s Lantern</div>
  <div style="position:absolute;left:28px;top:64px;font-weight:700;font-size:10.5px;color:var(--plum-deep)">Heading Title Here</div>
  <div style="position:absolute;left:24px;top:84px;width:441px;font-size:7px">
    <div style="display:flex;height:35px;margin-bottom:6px;background:#fff;border-radius:4px"><div style="flex:0 0 100px;background:#5d4874;border-radius:4px;color:#fff;font-weight:700;font-size:8px;padding:6px 0 0 40px;line-height:10px;position:relative"><span class="icon-dot" style="position:absolute;left:12px;top:9px;width:16px;height:16px"></span>Text Title<br>Content 1</div><div style="padding:6px 10px;line-height:9px">Lorem ipsum dolor sit amet, te ullum corpora delicata duo. Rebum insolens pri eu. No alia tota modus qui.</div></div>
    <div style="display:flex;height:35px;margin-bottom:6px;background:#fff;border-radius:4px"><div style="flex:0 0 100px;background:#7d6691;border-radius:4px;color:#fff;font-weight:700;font-size:8px;padding:6px 0 0 40px;line-height:10px;position:relative"><span class="icon-dot" style="position:absolute;left:12px;top:9px;width:16px;height:16px"></span>Text Title<br>Content 2</div><div style="padding:6px 10px;line-height:9px">Lorem ipsum dolor sit amet, te ullum corpora delicata duo. Rebum insolens pri eu. No alia tota modus qui.</div></div>
    <div style="display:flex;height:35px;margin-bottom:6px;background:#fff;border-radius:4px"><div style="flex:0 0 100px;background:#a68fb7;border-radius:4px;color:#fff;font-weight:700;font-size:8px;padding:6px 0 0 40px;line-height:10px;position:relative"><span class="icon-dot" style="position:absolute;left:12px;top:9px;width:16px;height:16px"></span>Text Title<br>Content 3</div><div style="padding:6px 10px;line-height:9px">Lorem ipsum dolor sit amet, te ullum corpora delicata duo. Rebum insolens pri eu. No alia tota modus qui.</div></div>
    <div style="display:flex;height:35px;background:#fff;border-radius:4px"><div style="flex:0 0 100px;background:#d3a3a2;border-radius:4px;color:#fff;font-weight:700;font-size:8px;padding:6px 0 0 40px;line-height:10px;position:relative"><span class="icon-dot" style="position:absolute;left:12px;top:9px;width:16px;height:16px"></span>Text Title<br>Content 4</div><div style="padding:6px 10px;line-height:9px">Lorem ipsum dolor sit amet, te ullum corpora delicata duo. Rebum insolens pri eu. No alia tota modus qui.</div></div>
  </div>
  <div class="page-no">5</div>
</section>

<!-- Divider -->
<section class="slide" style="left:78px;top:987px;background:linear-gradient(180deg,#5b4672,#74608a)">
  <svg class="waves" viewBox="0 0 488 275" preserveAspectRatio="none">
    <defs><linearGradient id="dv" x1="0" y1="0" x2="1" y2="1"><stop offset="0" stop-color="#e4b9b5"/><stop offset="1" stop-color="#b990bd"/></linearGradient></defs>
    <path d="M230 0 C240 40 330 50 300 120 C270 190 180 230 160 275 L488 275 L488 0Z" fill="url(#dv)" opacity=".85"/>
    <path d="M488 120 C420 160 360 220 330 275 L488 275Z" fill="#c69bbf" opacity=".5"/>
  </svg>
  <div class="flora" role="img" aria-label="Line-drawn floral sprig" style="left:150px;top:160px;width:80px;height:110px"></div>
  <div class="brand light top-right">Marigold’s Lantern</div>
  <div class="serif" style="position:absolute;left:24px;top:64px;font-size:20px;line-height:22px;color:#fff">Divider Slide<br>Title Here</div>
  <div style="position:absolute;left:24px;top:120px;width:190px;font-size:8.5px;line-height:11px;color:#fff">Lorem Ipsum is simply dummy text of the printing and typesetting industry.</div>
</section>

<!-- Three cards -->
<section class="slide" style="left:602px;top:987px;background:linear-gradient(135deg,#f6eef2,#f1dfe4)">
  <div class="flora pink" role="img" aria-label="Line-drawn floral sprig" style="left:0;top:170px;width:50px;height:100px"></div>
  <div class="slide-title">Presentation Title here</div>
  <div class="brand top-right">Marigold’s Lantern</div>
  <div style="position:absolute;left:30px;top:88px;display:flex;gap:11px;font-size:7.5px;line-height:8.5px">
    <article style="width:133px;height:140px;background:#fff;border-radius:6px;padding:38px 10px 0 10px;position:relative"><span class="icon-dot" style="position:absolute;left:36px;top:-32px;width:62px;height:62px;background:#5d4874"></span><div style="font-weight:800;color:var(--plum-deep);font-size:8px;margin-bottom:3px">Insert Your Heading text Goes Here</div><ul class="star-list" style="color:var(--plum)"><li>Lorem ipsum dolor sit amet, consectetur</li><li>Phasellus malesuada vulputate mauris,</li><li>vitae pretium felis vestibulum vel.</li></ul></article>
    <article style="width:133px;height:140px;background:#fff;border-radius:6px;padding:38px 10px 0 10px;position:relative"><span class="icon-dot" style="position:absolute;left:36px;top:-32px;width:62px;height:62px;background:#8a7399"></span><div style="font-weight:800;color:var(--plum-deep);font-size:8px;margin-bottom:3px">Insert Your Heading text Goes Here</div><ul class="star-list" style="color:var(--plum)"><li>Lorem ipsum dolor sit amet, consectetur</li><li>Phasellus malesuada vulputate mauris,</li><li>vitae pretium felis vestibulum vel.</li></ul></article>
    <article style="width:133px;height:140px;background:#fff;border-radius:6px;padding:38px 10px 0 10px;position:relative"><span class="icon-dot" style="position:absolute;left:36px;top:-32px;width:62px;height:62px;background:#d3a3a2"></span><div style="font-weight:800;color:var(--plum-deep);font-size:8px;margin-bottom:3px">Insert Your Heading text Goes Here</div><ul class="star-list" style="color:var(--plum)"><li>Lorem ipsum dolor sit amet, consectetur</li><li>Phasellus malesuada vulputate mauris,</li><li>vitae pretium felis vestibulum vel.</li></ul></article>
  </div>
  <div class="page-no">7</div>
</section>

<!-- 6 Point -->
<section class="slide" style="left:78px;top:1292px;background:var(--cream)">
  <svg class="waves" viewBox="0 0 488 275" preserveAspectRatio="none">
    <path d="M488 180 C440 190 420 230 350 245 C320 252 300 262 290 275 L488 275Z" fill="#ecc6c3" opacity=".8"/>
  </svg>
  <div class="slide-title">6 Poin Content</div>
  <div class="brand top-right">Marigold’s Lantern</div>
  <div style="position:absolute;left:24px;top:62px;display:grid;grid-template-columns:repeat(3,140px);gap:10px;font-size:5.3px;line-height:6px">
    <div style="background:#fff;border-radius:4px;height:82px"><div style="background:#7d6691;color:#fff;font-weight:700;font-size:8px;padding:5px 12px;border-radius:4px 4px 0 0">Heading Text 1</div><p style="padding:6px 12px">Lorem Ipsum has been the industry’s standard dummy text ever since the 1500s, when an unknown printer took a galley of type and scrambled it to make a type specimen book.</p></div>
    <div style="background:#fff;border-radius:4px;height:82px"><div style="background:#cf9d9b;color:#fff;font-weight:700;font-size:8px;padding:5px 12px;border-radius:4px 4px 0 0">Heading Text 2</div><p style="padding:6px 12px">Lorem Ipsum has been the industry’s standard dummy text ever since the 1500s, when an unknown printer took a galley of type and scrambled it to make a type specimen book.</p></div>
    <div style="background:#fff;border-radius:4px;height:82px"><div style="background:#7d6691;color:#fff;font-weight:700;font-size:8px;padding:5px 12px;border-radius:4px 4px 0 0">Heading Text 3</div><p style="padding:6px 12px">Lorem Ipsum has been the industry’s standard dummy text ever since the 1500s, when an unknown printer took a galley of type and scrambled it to make a type specimen book.</p></div>
    <div style="background:#fff;border-radius:4px;height:82px"><div style="background:#cf9d9b;color:#fff;font-weight:700;font-size:8px;padding:5px 12px;border-radius:4px 4px 0 0">Heading Text 4</div><p style="padding:6px 12px">Lorem Ipsum has been the industry’s standard dummy text ever since the 1500s, when an unknown printer took a galley of type and scrambled it to make a type specimen book.</p></div>
    <div style="background:#fff;border-radius:4px;height:82px"><div style="background:#7d6691;color:#fff;font-weight:700;font-size:8px;padding:5px 12px;border-radius:4px 4px 0 0">Heading Text 5</div><p style="padding:6px 12px">Lorem Ipsum has been the industry’s standard dummy text ever since the 1500s, when an unknown printer took a galley of type and scrambled it to make a type specimen book.</p></div>
    <div style="background:#fff;border-radius:4px;height:82px"><div style="background:#cf9d9b;color:#fff;font-weight:700;font-size:8px;padding:5px 12px;border-radius:4px 4px 0 0">Heading Text 6</div><p style="padding:6px 12px">Lorem Ipsum has been the industry’s standard dummy text ever since the 1500s, when an unknown printer took a galley of type and scrambled it to make a type specimen book.</p></div>
  </div>
  <div class="page-no">8</div>
</section>

<!-- Content with image -->
<section class="slide" style="left:602px;top:1292px;background:#f4f0f4">
  <svg class="waves" viewBox="0 0 488 275" preserveAspectRatio="none">
    <defs><linearGradient id="ci" x1="0" y1="0" x2="0" y2="1"><stop offset="0" stop-color="#8a6f9c"/><stop offset="1" stop-color="#5b4672"/></linearGradient></defs>
    <path d="M420 0 C380 20 380 80 320 120 C260 160 230 230 190 275 L488 275 L488 0Z" fill="url(#ci)"/>
    <path d="M488 190 C420 195 370 230 300 240 C280 245 265 260 260 275 L488 275Z" fill="#dfa9a6"/>
  </svg>
  <div class="flora" role="img" aria-label="Line-drawn botanical stems" style="left:350px;top:50px;width:110px;height:220px"></div>
  <div class="slide-title">Content with Image sample</div>
  <div class="brand light top-right">Marigold’s Lantern</div>
  <div style="position:absolute;left:28px;top:62px;font-weight:700;font-size:10.5px;color:var(--plum-deep)">Lorem Ipsum</div>
  <div style="position:absolute;left:28px;top:80px;width:220px;font-size:8.5px;line-height:10px">
    <ul class="star-list"><li>Lorem ipsum dolor sit amet,<br>te ullum corpora delicata duo.<br>Rebum insolens pri eu.<br>No alia tota modus qui.</li></ul>
    <ul class="star-list" style="margin:2px 0 10px 18px;font-size:7.5px;line-height:9px"><li>Sint brute at usu. Duo iisque appareat adversarium at.</li></ul>
    <ul class="star-list"><li>Lorem ipsum dolor sit amet,<br>te ullum corpora delicata duo.<br>Rebum insolens pri eu.<br>No alia tota modus qui.</li></ul>
    <ul class="star-list" style="margin:2px 0 0 18px;font-size:7.5px;line-height:9px"><li>Sint brute at usu. Duo iisque appareat adversarium at.</li></ul>
  </div>
  <div class="page-no" style="color:#fff">9</div>
</section>

<!-- Presentation Title Here (text + boxes) -->
<section class="slide" style="left:78px;top:1597px;background:var(--cream)">
  <div class="slide-title">Presentation Title Here</div>
  <div class="brand top-right">Marigold’s Lantern</div>
  <ul class="star-list" style="position:absolute;left:26px;top:60px;width:165px;font-size:8.5px;line-height:9.5px">
    <li style="margin-bottom:8px">Lorem ipsum dolor sit amet, consectetur adipiscing elit. Phasellus malesuada vulputate mauris, vitae pretium felis vestibulum vel. Vestibulum non sagittis orci. Fusce finibus elit et felis imperdiet</li>
    <li>Lorem ipsum dolor sit amet, consectetur adipiscing elit. Phasellus malesuada vulputate mauris, vitae pretium felis vestibulum vel. Vestibulum non sagittis orci. Fusce finibus elit et felis imperdiet</li>
  </ul>
  <div style="position:absolute;left:198px;top:60px;display:flex;gap:8px;font-size:6px;line-height:7px;color:var(--plum-mid)">
    <div style="width:129px;height:124px;background:#eadde5;border-radius:6px;padding:44px 10px 0"><span class="icon-dot" style="position:absolute;margin:-34px 0 0 0;width:20px;height:20px;background:var(--plum-mid)"></span>Lorem ipsum dolor sit amet, consectetur adipiscing elit. Phasellus malesuada vulputate mauris, vitae pretium felis vestibulum vel. Vestibulum non sagittis orci. Fusce finibus elit et felis imperdiet</div>
    <div style="width:129px;height:124px;background:#f1e2e3;border-radius:6px;padding:44px 10px 0"><span class="icon-dot" style="position:absolute;margin:-34px 0 0 0;width:20px;height:20px;background:var(--blush)"></span>Lorem ipsum dolor sit amet, consectetur adipiscing elit. Phasellus malesuada vulputate mauris, vitae pretium felis vestibulum vel. Vestibulum non sagittis orci. Fusce finibus elit et felis imperdiet</div>
  </div>
  <div style="position:absolute;left:198px;top:192px;width:266px;height:42px;background:#a48fb8;border-radius:6px;color:#fff;font-size:6.3px;line-height:7.5px;padding:8px 14px 0 30px">Lorem ipsum dolor sit amet, consectetur adipiscing elit. Phasellus malesuada vulputate mauris, vitae pretium felis vestibulum vel.<div style="text-align:right">- Lorem Ipsum</div></div>
  <div class="flora pink" role="img" aria-label="Line-drawn floral sprig" style="left:190px;top:220px;width:50px;height:55px"></div>
  <div class="page-no">10</div>
</section>

<!-- About Us -->
<section class="slide" style="left:602px;top:1597px;background:var(--cream)">
  <div class="slide-title">About Us</div>
  <div class="brand top-right">Marigold’s Lantern</div>
  <div style="position:absolute;left:24px;top:60px;display:flex;gap:9px;font-size:6px;line-height:7px;color:var(--plum)">
    <div style="width:104px;height:154px;border-radius:6px;background:linear-gradient(180deg,#e6d8e3,#ecdbe0);padding:12px 8px"><div style="display:flex;gap:8px;align-items:center;font-weight:700;font-size:9.5px;line-height:10px;color:var(--plum-mid);margin-bottom:20px"><span class="icon-dot" style="width:18px;height:18px;background:var(--lavender)"></span>Heading<br>Text 1</div>Lorem ipsum dolor sit amet, consectetur adipiscing elit. Phasellus malesuada vulputate mauris, vitae pretium felis vestibulum vel. Vestibulum non sagittis orci. Fusce finibus elit et felis imperdiet</div>
    <div style="width:104px;height:154px;border-radius:6px;background:linear-gradient(180deg,#e6d8e3,#ecdbe0);padding:12px 8px"><div style="display:flex;gap:8px;align-items:center;font-weight:700;font-size:9.5px;line-height:10px;color:var(--plum-mid);margin-bottom:20px"><span class="icon-dot" style="width:18px;height:18px;background:var(--blush)"></span>Heading<br>Text 2</div>Lorem ipsum dolor sit amet, consectetur adipiscing elit. Phasellus malesuada vulputate mauris, vitae pretium felis vestibulum vel. Vestibulum non sagittis orci. Fusce finibus elit et felis imperdiet</div>
    <div style="width:104px;height:154px;border-radius:6px;background:linear-gradient(180deg,#e6d8e3,#ecdbe0);padding:12px 8px"><div style="display:flex;gap:8px;align-items:center;font-weight:700;font-size:9.5px;line-height:10px;color:var(--plum-mid);margin-bottom:20px"><span class="icon-dot" style="width:18px;height:18px;background:var(--plum-mid)"></span>Heading<br>Text 3</div>Lorem ipsum dolor sit amet, consectetur adipiscing elit. Phasellus malesuada vulputate mauris, vitae pretium felis vestibulum vel. Vestibulum non sagittis orci. Fusce finibus elit et felis imperdiet</div>
    <div style="width:104px;height:154px;border-radius:6px;background:linear-gradient(180deg,#e6d8e3,#ecdbe0);padding:12px 8px"><div style="display:flex;gap:8px;align-items:center;font-weight:700;font-size:9.5px;line-height:10px;color:var(--plum-mid);margin-bottom:20px"><span class="icon-dot" style="width:18px;height:18px;background:var(--blush)"></span>Heading<br>Text 4</div>Lorem ipsum dolor sit amet, consectetur adipiscing elit. Phasellus malesuada vulputate mauris, vitae pretium felis vestibulum vel. Vestibulum non sagittis orci. Fusce finibus elit et felis imperdiet</div>
  </div>
  <div style="position:absolute;left:24px;top:225px;width:441px;height:18px;border-radius:9px;background:#a995be;color:#fff;font-size:9px;text-align:center;line-height:18px">Lorem ipsum dolor sit amet, consectetur adipiscing elit.</div>
  <div class="page-no">11</div>
</section>

<!-- Quote -->
<section class="slide" style="left:78px;top:1903px;background:linear-gradient(160deg,#55416c,#7f6892)">
  <div role="img" aria-label="Faint interconnected web of support pattern" style="position:absolute;left:200px;top:0;width:288px;height:275px;background:radial-gradient(circle at 60% 50%,rgba(255,255,255,.08),rgba(255,255,255,0) 65%)"></div>
  <div class="brand light top-right">Marigold’s Lantern</div>
  <div class="serif" style="position:absolute;left:24px;top:52px;font-size:46px;line-height:46px;color:var(--blush)">“</div>
  <blockquote style="position:absolute;left:24px;top:98px;width:222px;font-weight:800;font-size:12.5px;line-height:15px;color:#fff">Lorem Ipsum has been the industry’s standard dummy text ever since the 1500s, when an unknown printer took a galley of type and scrambled it to make a type specimen book.</blockquote>
  <div style="position:absolute;left:24px;top:200px;font-size:8.5px;color:var(--blush-soft)">John Doe</div>
  <div class="page-no" style="color:#fff">12</div>
</section>

<!-- Graphic Process (Venn) -->
<section class="slide" style="left:602px;top:1903px;background:var(--cream)">
  <div class="slide-title">Graphic Process Sample</div>
  <div class="brand top-right">Marigold’s Lantern</div>
  <svg style="position:absolute;left:150px;top:55px" width="190" height="200" viewBox="0 0 190 200">
    <circle cx="67" cy="67" r="60" fill="#7d6691" opacity=".9"/>
    <circle cx="123" cy="67" r="60" fill="#cf9a98" opacity=".85"/>
    <circle cx="95" cy="135" r="60" fill="#f2dcdd" opacity=".9"/>
  </svg>
  <div class="venn-label" style="left:20px;top:80px;text-align:right"><h4 style="color:var(--plum-mid)">Heading Text 1</h4>Lorem Ipsum has been the industry’s standard dummy text ever since the 1500s, when an unknown printer took a galley of type and scrambled it to make a type specimen book.</div>
  <div class="venn-label" style="left:340px;top:80px"><h4 style="color:var(--blush)">Heading Text 2</h4>Lorem Ipsum has been the industry’s standard dummy text ever since the 1500s, when an unknown printer took a galley of type and scrambled it to make a type specimen book.</div>
  <div class="venn-label" style="left:50px;top:172px;text-align:right"><h4 style="color:#e3aaa8">Heading Text 3</h4>Lorem Ipsum has been the industry’s standard dummy text ever since the 1500s, when an unknown printer took a galley of type and scrambled it to make a type specimen book.</div>
  <div class="page-no">13</div>
</section>

<!-- Timeline -->
<section class="slide" style="left:78px;top:2209px;background:var(--cream)">
  <div class="slide-title">Timeline Sample</div>
  <div class="brand top-right">Marigold’s Lantern</div>
  <div style="position:absolute;left:70px;top:92px;width:345px;height:1.5px;background:var(--blush-soft)"></div>
  <div style="position:absolute;left:28px;top:64px;display:flex;gap:29px;text-align:center;font-size:8.5px;line-height:10px">
    <div style="width:56px"><span class="icon-dot" style="width:56px;height:56px;background:#5d4874;display:flex"></span><div style="font-weight:700;margin:12px 0 3px;color:var(--ink)">Jan 2026</div>Lorem ipsum dolor sit amet, te ullum corpora delicata duo.</div>
    <div style="width:56px"><span class="icon-dot" style="width:56px;height:56px;background:#e2b3b1;display:flex"></span><div style="font-weight:700;margin:12px 0 3px;color:var(--ink)">Feb 2026</div>Lorem ipsum dolor sit amet, te ullum corpora delicata duo.</div>
    <div style="width:56px"><span class="icon-dot" style="width:56px;height:56px;background:#5d4874;display:flex"></span><div style="font-weight:700;margin:12px 0 3px;color:var(--ink)">Mar 2026</div>Lorem ipsum dolor sit amet, te ullum corpora delicata duo.</div>
    <div style="width:56px"><span class="icon-dot" style="width:56px;height:56px;background:#e2b3b1;display:flex"></span><div style="font-weight:700;margin:12px 0 3px;color:var(--ink)">Apr 2026</div>Lorem ipsum dolor sit amet, te ullum corpora delicata duo.</div>
    <div style="width:56px"><span class="icon-dot" style="width:56px;height:56px;background:#5d4874;display:flex"></span><div style="font-weight:700;margin:12px 0 3px;color:var(--ink)">May 2026</div>Lorem ipsum dolor sit amet, te ullum corpora delicata duo.</div>
  </div>
  <div class="flora pink" role="img" aria-label="Line-drawn floral sprig" style="left:410px;top:180px;width:75px;height:95px"></div>
  <div class="page-no">14</div>
</section>

<!-- Thank You -->
<section class="slide" style="left:602px;top:2209px;background:linear-gradient(180deg,#5b4672,#6f5985)">
  <svg class="waves" viewBox="0 0 488 275" preserveAspectRatio="none">
    <defs><linearGradient id="ty" x1="0" y1="0" x2="1" y2="1"><stop offset="0" stop-color="#e2b4b0"/><stop offset="1" stop-color="#a886ad"/></linearGradient></defs>
    <path d="M250 0 C230 40 200 60 210 110 C220 160 250 220 240 275 L488 275 L488 0Z" fill="url(#ty)" opacity=".8"/>
    <path d="M340 0 C310 60 360 120 300 190 C270 225 250 250 240 275 L488 275 L488 0Z" fill="#6e5785" opacity=".85"/>
  </svg>
  <div class="flora" role="img" aria-label="Line-drawn floral sprig" style="left:300px;top:60px;width:130px;height:210px"></div>
  <div class="brand light" style="left:24px;top:62px">Marigold’s Lantern</div>
  <div class="serif" style="position:absolute;left:24px;top:96px;font-size:21px;color:var(--blush-soft)">Thank You</div>
  <p style="position:absolute;left:24px;top:135px;width:150px;font-size:7.5px;line-height:9px;color:#fff">Lorem ipsum dolor sit amet, te ullum corpora delicata duo. Rebum insolens pri eu. No alia tota modus qui.</p>
  <ul style="position:absolute;left:24px;top:178px;list-style:none;font-size:6.5px;color:#fff">
    <li style="display:flex;align-items:center;gap:6px;height:21px"><span style="width:10px;height:10px;border-radius:50%;background:var(--lavender)"></span>yourmail@website.com</li>
    <li style="display:flex;align-items:center;gap:6px;height:21px"><span style="width:10px;height:10px;border-radius:50%;background:var(--lavender)"></span>+1234 5678 910</li>
    <li style="display:flex;align-items:center;gap:6px;height:21px"><span style="width:10px;height:10px;border-radius:50%;background:var(--lavender)"></span>www.marigoldslanterncare.org</li>
  </ul>
</section>

</body>
</html>
```